Design a wedding invitation

I need a classic and beautiful wedding invitation design URGENTLY
I have uploaded some example invitations where I like the LAYOUT only - PLESE REFER TO THIS LAYOUT FOR IMAGE, LOGO AND TEXT !
The imagery is in the other file uploaded - there are two options for the imagery whichever one works best with the layout
I would like to include some sort of logo of our initials H&L if possible
Size is A5
I would like to keep the same colour palette as the artworks
I do not want to make the Vantrel Arch the centre of the design we are looking for a more subtle effect
We want to avoid the look of 'image at the bottom and text at the top' by creating one unified piece
The final design will be letterpress printed with embossing so image cannot overlap with text
The wording is as follows:

“The honour of your presence
is requested at the wedding of Lucinda Marsh to Henrik Dalvang
Saturday, the eighth of September Two thousand and eighteen
at six o’clock in the evening
Château du Q
Paris, France
Black Tie"

```html
<!DOCTYPE html>
<html lang="en">
<head>
<meta charset="utf-8">
<title>Wedding Invitation — Lucinda Marsh &amp; Henrik Dalvang</title>
<link rel="stylesheet" href="https://fonts.googleapis.com/css2?family=Cinzel:wght@400&family=Pinyon+Script&display=swap">
<style>
  :root {
    --backdrop: #d9d9db;
    --paper: #fbfbfa;
    --ink: #4a4848;
    --rose: #c23f6c;
    --shadow: rgba(0,0,0,0.18);
  }
  * { margin: 0; padding: 0; box-sizing: border-box; }
  html, body {
    width: 1200px; height: 1200px; overflow: hidden;
    background: var(--backdrop);
  }
  .canvas { position: relative; width: 1200px; height: 1200px; }
  .invitation {
    position: absolute; left: 204px; top: 40px;
    width: 792px; height: 1120px;
    background: var(--paper);
    box-shadow: 0 10px 30px var(--shadow);
    overflow: hidden;
  }
  .invitation__artwork {
    position: absolute; inset: 0; width: 792px; height: 1120px;
  }
  .invitation__text {
    position: absolute; left: 350px; top: 62px; width: 380px;
    text-align: center; color: var(--ink);
  }
  .monogram {
    font-family: "Pinyon Script", cursive;
    font-size: 64px; line-height: 1; color: var(--rose);
    margin-bottom: 40px;
  }
  .caps {
    font-family: "Cinzel", serif;
    font-size: 15.5px; line-height: 24px; letter-spacing: 0.3px;
    text-transform: uppercase;
  }
  .couple {
    font-family: "Pinyon Script", cursive;
    color: var(--rose); margin: 14px 0 16px;
  }
  .couple__name { display: block; font-size: 46px; line-height: 56px; }
  .couple__join { display: block; font-size: 28px; line-height: 30px; }
  .dress-code {
    font-family: "Pinyon Script", cursive;
    font-size: 34px; line-height: 1; color: var(--rose);
    margin-top: 14px;
  }
</style>
</head>
<body>
<main class="canvas">
  <article class="invitation">
    <svg class="invitation__artwork" viewBox="0 0 792 1120" role="img"
         aria-label="Soft grey and rose painted Paris street scene: a blossoming tree at left, a couple walking beneath pink blossoms, street lamps, townhouses and the Vantrel Arch in the distance">
      <defs>
        <linearGradient id="scene-tone" x1="0" y1="0" x2="0" y2="1">
          <stop offset="0" stop-color="#ececec"/>
          <stop offset="0.4" stop-color="#c4c4c4"/>
          <stop offset="1" stop-color="#8a8a8a"/>
        </linearGradient>
        <radialGradient id="blossom-centre" cx="0.5" cy="0.66" r="0.28">
          <stop offset="0" stop-color="#d98aa6" stop-opacity="0.7"/>
          <stop offset="1" stop-color="#d98aa6" stop-opacity="0"/>
        </radialGradient>
        <radialGradient id="blossom-right" cx="0.92" cy="0.52" r="0.14">
          <stop offset="0" stop-color="#d98aa6" stop-opacity="0.55"/>
          <stop offset="1" stop-color="#d98aa6" stop-opacity="0"/>
        </radialGradient>
        <filter id="feather" x="-10%" y="-10%" width="120%" height="120%">
          <feGaussianBlur stdDeviation="22"/>
        </filter>
      </defs>
      <g filter="url(#feather)">
        <path class="scene-area" d="M-40,170 C140,120 290,170 320,330 C340,450 350,560 420,650 C500,720 580,660 650,580 C710,520 760,490 840,470 L840,1160 L-40,1160 Z" fill="url(#scene-tone)"/>
        <path d="M-40,170 C140,120 290,170 320,330 C340,450 350,560 420,650 C500,720 580,660 650,580 C710,520 760,490 840,470 L840,1160 L-40,1160 Z" fill="url(#blossom-centre)"/>
        <path d="M-40,170 C140,120 290,170 320,330 C340,450 350,560 420,650 C500,720 580,660 650,580 C710,520 760,490 840,470 L840,1160 L-40,1160 Z" fill="url(#blossom-right)"/>
      </g>
    </svg>

    <div class="invitation__text">
      <div class="monogram">H&amp;L</div>
      <p class="caps">The honour of your presence<br>is requested at the wedding of</p>
      <p class="couple">
        <span class="couple__name">Lucinda Marsh</span>
        <span class="couple__join">to</span>
        <span class="couple__name">Henrik Dalvang</span>
      </p>
      <p class="caps">
        Saturday, the eighth of September<br>
        Two thousand and eighteen<br>
        at six o’clock in the evening<br>
        Château du Q<br>
        Paris, France
      </p>
      <p class="dress-code">Black Tie</p>
    </div>
  </article>
</main>
</body>
</html>
```